Business Card Design Project

Taprilo - based in Melbourne, Australia. We plan, design, implement and support network infrastructure (Vorda, Halvest, K8, Tarnwick etc).

Target Market(s)

Small/Medium enterprise and Corporate.

Industry/Entity Type

Business

```html
<!DOCTYPE html>
<html lang="en">
<head>
<meta charset="utf-8">
<title>Taprilo Business Card</title>
<link href="https://fonts.googleapis.com/css2?family=Lato:wght@400;700;900&display=swap" rel="stylesheet">
<style>
  :root {
    --backdrop: #e9e6e2;
    --card-dark: #1e1e1e;
    --card-light: #ffffff;
    --brand-orange: #e07118;
    --ink: #1c1c1c;
    --slab: #222222;
  }
  * { margin: 0; padding: 0; box-sizing: border-box; }
  html, body { width: 1200px; height: 900px; overflow: hidden; }
  body {
    background: var(--backdrop);
    font-family: "Lato", Arial, sans-serif;
    position: relative;
  }
  .card {
    position: absolute;
    left: 250px;
    width: 700px;
    height: 400px;
    box-shadow: 0 8px 22px rgba(0,0,0,0.22);
    overflow: hidden;
  }
  .card--front { top: 35px; background: var(--card-dark); }
  .card--back { top: 465px; background: var(--card-light); }

  .brand {
    position: absolute;
    display: flex;
    align-items: center;
    gap: 14px;
    font-weight: 700;
    letter-spacing: 1px;
  }
  .brand__dot { border-radius: 50%; background: var(--brand-orange); }
  .card--front .brand {
    left: 50%; top: 50%;
    transform: translate(-50%, -50%);
    color: #ffffff;
    font-size: 64px;
  }
  .card--front .brand__dot { width: 62px; height: 62px; }

  .card--back .brand {
    left: 50%; top: 72px;
    transform: translateX(-50%);
    color: var(--ink);
    font-size: 44px;
  }
  .card--back .brand__dot { width: 42px; height: 42px; }

  .address {
    position: absolute;
    left: 50%; top: 140px;
    transform: translateX(-50%);
    font-size: 17px;
    font-weight: 700;
    color: var(--ink);
    white-space: nowrap;
    padding: 0 6px 6px;
    border-bottom: 2px solid var(--brand-orange);
  }

  .holder {
    position: absolute;
    right: 36px; top: 200px;
    text-align: left;
  }
  .holder__name { color: var(--brand-orange); font-size: 20px; font-weight: 400; letter-spacing: 0.5px; }
  .holder__role { color: var(--ink); font-size: 17px; font-weight: 700; }

  .shapes { position: absolute; inset: 0; }

  .contact {
    position: absolute;
    list-style: none;
    font-size: 16px;
    font-weight: 700;
    color: var(--ink);
  }
  .contact li { display: flex; align-items: center; gap: 10px; height: 22px; }
  .contact svg { width: 18px; height: 16px; flex: none; }
  .contact--phones { left: 36px; top: 300px; }
  .contact--web { left: 312px; top: 222px; }
</style>
</head>
<body>
  <section class="card card--front" aria-label="Card front">
    <div class="brand"><span class="brand__dot"></span>taprilo</div>
  </section>

  <section class="card card--back" aria-label="Card back">
    <svg class="shapes" viewBox="0 0 700 400" aria-hidden="true">
      <polygon points="0,345 300,345 318,270 535,270 527,345 700,345 700,400 0,400" fill="var(--brand-orange)"/>
      <polygon points="553,262 700,262 700,345 543,345" fill="var(--slab)"/>
    </svg>

    <div class="brand"><span class="brand__dot"></span>taprilo</div>
    <p class="address">Street 1,City Name&nbsp; Harbor Vale, NV 60412</p>

    <div class="holder">
      <p class="holder__name">MARA ELLIS</p>
      <p class="holder__role">Manager</p>
    </div>

    <ul class="contact contact--web">
      <li>
        <svg viewBox="0 0 18 16"><rect x="1" y="3" width="16" height="11" fill="var(--brand-orange)"/><polyline points="1,3 9,10 17,3" fill="none" stroke="#fff" stroke-width="1.5"/></svg>
        maraellis@taprilo.com
      </li>
      <li>
        <svg viewBox="0 0 18 16"><rect x="1.5" y="1.5" width="15" height="10" fill="none" stroke="var(--brand-orange)" stroke-width="2"/><rect x="6" y="13" width="6" height="2" fill="var(--brand-orange)"/></svg>
        www.taprilo.com
      </li>
    </ul>

    <ul class="contact contact--phones">
      <li>
        <svg viewBox="0 0 18 16"><path d="M2 6 Q9 -1 16 6 L13 8 L11 5 L7 5 L5 8 Z" fill="var(--brand-orange)"/><rect x="4" y="9" width="10" height="6" rx="1" fill="var(--brand-orange)"/></svg>
        +100 555 0142
      </li>
      <li>
        <svg viewBox="0 0 18 16"><rect x="5" y="1" width="8" height="4" fill="var(--brand-orange)"/><rect x="1" y="6" width="16" height="6" rx="1" fill="var(--brand-orange)"/><rect x="5" y="10" width="8" height="5" fill="var(--brand-orange)" stroke="#fff" stroke-width="1"/></svg>
        +100 555 0178
      </li>
    </ul>
  </section>
</body>
</html>
```